Kestrel Vitality a Centre Pty Ltd

Business card is to promote and represent our new business. It's situated in
47 Fenwick Road
Brookvale 2100 Sydney
Our clinic is all about getting people back to great health giving them back their lifestyle in half the usual time it takes to get results elsewhere , we do this through innovative therapies with latest state of the art equipment ,skills ,knowledge and experience.
We give them back their pain free healthy lifestyle with lots of energy to love life and perform their best Quickly and effectively .
The final design should communicate
Trust , confidence, results .
Updates

Reason: Waiting for some designers to submit work Thanks

Target Market(s)

High end clients that take their health and results seriously ,
High end athletes , as well as general people that want to see results with different
Treatment Methods and approach

Industry/Entity Type

Clinic

Contact Information for Business Card

Kestrel Vitality Centre Pty Ltd
47 Fenwick Road Brookvale 2100 Sydney
Website www.kestrelvitalitycentre.com.au

Font styles to use
Other font styles liked:
• Gothic font medium

Requirements
Must have
• A designe that makes people look twice with a wow factor , a designe that isn't like all the rest .
• Must have the logo in the colours Iv provided in my files
• Must communicate Trust, confidence , results
Nice to have
• 1) The logo raised up or
• 2) Maybe a pop up logo on the card ?
• Or let's be creative and have two cards one on top of the other so the two cards slide .... The front will have the kestrel logo with the address details etc
• The other card with have
• eg your next app .......................................repeating all way down the card
Should not have
• Basic plain looking card that everyone else has

```html
<!DOCTYPE html>
<html lang="en">
<head>
<meta charset="utf-8">
<title>Kestrel Vitality Centre – Business Card</title>
<link href="https://fonts.googleapis.com/css2?family=Marcellus+SC&display=swap" rel="stylesheet">
<style>
  :root {
    --backdrop: #e9eaeb;
    --card-white: #ffffff;
    --band-grey: #58595b;
    --brand-green: #7cc242;
    --card-w: 680px;
    --card-h: 390px;
  }
  * { margin: 0; padding: 0; box-sizing: border-box; }
  html, body {
    width: 1200px;
    height: 1000px;
    overflow: hidden;
    background: var(--backdrop);
  }
  .canvas {
    position: relative;
    width: 1200px;
    height: 1000px;
  }
  .card {
    position: absolute;
    left: 260px;
    width: var(--card-w);
    height: var(--card-h);
    background: var(--band-grey);
    border-radius: 4px;
    overflow: hidden;
    box-shadow: 0 6px 18px rgba(0,0,0,0.18);
    font-family: "Marcellus SC", "Times New Roman", serif;
    color: var(--brand-green);
  }
  .card--front { top: 85px; }
  .card--back { top: 525px; }

  .panel {
    position: absolute;
    background: var(--card-white);
  }
  .panel--top {
    top: 0;
    right: 0;
    left: 15%;
    height: 30%;
    border-bottom-left-radius: 20px;
  }
  .panel--bottom {
    left: 0;
    bottom: 0;
    width: 86%;
    top: 57%;
    border-top-right-radius: 20px;
  }

  .company-name {
    position: absolute;
    left: 0;
    right: 0;
    text-align: center;
    font-size: 26px;
    letter-spacing: 0.5px;
    white-space: nowrap;
  }
  .card--front .company-name { top: 58px; }
  .card--back .company-name { top: 80px; }

  .brand-mark {
    position: absolute;
    display: flex;
    align-items: center;
    gap: 12px;
    font-size: 34px;
    color: var(--brand-green);
  }
  .brand-mark__dot {
    width: 26px;
    height: 26px;
    border-radius: 50%;
    background: var(--brand-green);
  }
  .card--front .brand-mark { left: 28px; top: 158px; }
  .card--back .brand-mark {
    left: 50%;
    top: 158px;
    transform: translateX(-50%);
  }

  .contact {
    position: absolute;
    left: 96px;
    top: 62px;
    font-size: 22px;
    font-style: normal;
    line-height: 1.35;
    letter-spacing: 0.3px;
    white-space: nowrap;
  }
</style>
</head>
<body>
  <main class="canvas">
    <section class="card card--front" aria-label="Business card front">
      <div class="panel panel--top">
        <p class="company-name">Kestrel Vitality Centre Pty Ltd</p>
      </div>
      <div class="brand-mark">
        <span class="brand-mark__dot"></span>
        <span class="brand-mark__name">Kestrel</span>
      </div>
      <div class="panel panel--bottom">
        <address class="contact">
          <span class="contact__address">Fenwick Road Ashdale Norbury</span><br>
          <span class="contact__web">www.kestrelvitalitycentre.com.au</span>
        </address>
      </div>
    </section>

    <section class="card card--back" aria-label="Business card back">
      <div class="panel panel--top"></div>
      <div class="brand-mark">
        <span class="brand-mark__dot"></span>
        <span class="brand-mark__name">Kestrel</span>
      </div>
      <div class="panel panel--bottom">
        <p class="company-name">Kestrel Vitality Centre Pty Ltd</p>
      </div>
    </section>
  </main>
</body>
</html>
```